Texas Marsh Reed Conservation League

We need to design the home page of this new website. We would like a fun website design for provides as a resource for members and information for potential members.
Please design so that we can see a portion of background on each side on the website.
I just need the final design files psd no coding needed.
Attached is their logo (colors are not 100% set in stone either so can mess with those as I did in the quick mockup attached)
Attached is a pdf newsletter they send out, you can get a feel for them and what they are about. The design is crappy and we are here to fix that going forward and we are starting with the website.
Here are some quick example websites (design style is open)
- I attached a quick mockup i did just for a content visual but by all means do what you want.
- http://www.lonestarbizladies.org/
- http://www.wqrtf.org/
- http://demo.webkitpalette.com/demo.php?cat=html5themes&host=layoutbazaar&temp=veltrona
- http://www.fieldkeep.org/
- http://www.urbanpantry.org/
- http://www.projectcozy.org/
here are some of the other chapters website (pretty bad!)
and here are some of the others:
- http://www.kdwrcl.org/
- http://wrcl.org/
- http://www.gwrcl.org/
Content Items that need to be included:
1. Logo
2. Menu - home, about, members, resources, events, membership, contact
3. Become a member - button or action
4. social links - facebook, linkedin, youtube
5. banner - that needs to explain their purpose "Promoting environmental stewardship through operations, research, education and outreach" (or this can be worked into the design)
6. Upcoming event (s)
7. Advertisement - members can place an ad on the website, this can be a placeholder for now
8. newsletter signup
9. advertise with us - this link can be in the footer
30-60 years of age, succesfull (household budgets of 120K+ men and women that live in texas.
Education

```html
<!DOCTYPE html>
<html lang="en">
<head>
<meta charset="utf-8">
<title>Texas Marsh Reed Conservation League</title>
<link rel="stylesheet" href="https://fonts.googleapis.com/css2?family=Antonio:wght@400&family=Lato:ital,wght@0,400;0,700;1,400&family=Roboto+Condensed:wght@400&display=swap">
<style>
:root{
  --wine:#8a1f35;
  --wine-dark:#6e1528;
  --navy:#0d2a63;
  --navy-dark:#0a1f4a;
  --ink:#444;
  --muted:#666;
  --rule:#d8d8d8;
  --band:#e6e6e6;
  --foot:#3c3c3c;
  --foot-dark:#232323;
  --white:#fff;
}
*{box-sizing:border-box;margin:0;padding:0}
html,body{width:1151px;height:1200px;overflow:hidden}
body{font-family:"Lato",sans-serif;color:var(--ink);background:#cfdce6}
.page{width:1280px;height:1335px;position:relative;transform:scale(0.8992);transform-origin:0 0;
  background:linear-gradient(180deg,#eef3f8 0%,#dbe6ef 30%,#b9c9a6 45%,#7f9c6c 52%,#6d8fb0 60%,#9aa98a 78%,#c9cfb0 100%)}
a{text-decoration:none;color:inherit}
.account-tab{position:absolute;left:793px;top:0;width:345px;height:37px;background:var(--wine);
  clip-path:polygon(0 0,100% 0,93% 100%,7% 100%);display:flex;justify-content:center;align-items:center;gap:34px;
  color:var(--white);font-weight:700;font-size:14px}
.account-tab span{display:flex;align-items:center;gap:6px}
.brand{position:absolute;left:150px;top:36px;display:flex;align-items:center;gap:16px}
.brand-mark{width:62px;height:62px;border-radius:50%;background:var(--navy)}
.brand-short{font-family:"Roboto Condensed",sans-serif;font-size:40px;color:var(--wine)}
.site-title{position:absolute;left:383px;top:56px;font-family:"Roboto Condensed",sans-serif;font-size:24px;color:var(--wine);white-space:nowrap}
.main-nav{position:absolute;left:140px;top:105px;width:1000px;height:60px;background:linear-gradient(180deg,#163a7f,var(--navy-dark));
  border-top:3px solid #2a56a8;display:flex;align-items:center;padding-left:212px}
.main-nav a{color:var(--white);font-weight:700;font-size:16px;padding:9px 29px;border-radius:18px;margin-right:21px}
.main-nav a.current{background:var(--wine)}
.content{position:absolute;left:140px;top:165px;width:1000px;height:840px;background:var(--white)}
.slider{position:absolute;left:18px;top:18px;width:962px;height:412px;background:#eee;box-shadow:0 1px 3px rgba(0,0,0,.25)}
.slide-photo{position:absolute;left:7px;top:7px;width:950px;height:400px;
  background:linear-gradient(180deg,#b8d3ea 0%,#dbe8f2 28%,#5f8a3f 38%,#7ea35a 48%,#a7b7bd 58%,#6d8a74 75%,#8f9f55 100%)}
.slide-caption{position:absolute;left:43px;top:158px;width:715px;height:125px;background:rgba(255,255,255,.72);padding:14px 21px;
  font-family:"Antonio",sans-serif;line-height:50px;white-space:nowrap}
.slide-caption .lead{font-size:34px;color:#1d1d1d}
.slide-caption .focus{font-size:35px;color:var(--wine);text-transform:uppercase}
.slide-arrow{position:absolute;top:185px;width:48px;height:48px;border-radius:50%;background:rgba(255,255,255,.85);display:flex;align-items:center}
.slide-arrow.prev{left:-17px;justify-content:flex-end;padding-right:10px}
.slide-arrow.next{right:-17px;justify-content:flex-start;padding-left:10px}
.card{position:absolute;top:462px;width:298px;height:338px;background:var(--white);border:1px solid #e2e2e2;box-shadow:0 1px 3px rgba(0,0,0,.15);padding:14px 15px}
.card h2{font-family:"Roboto Condensed",sans-serif;font-weight:400;font-size:24px;color:var(--wine);padding-bottom:8px;border-bottom:1px solid var(--rule);position:relative}
.card h2 b{font-weight:400;color:var(--navy)}
.card h2::after{content:"";position:absolute;left:0;bottom:-2px;width:64px;height:3px;background:var(--wine)}
.about{left:20px}
.about .photo{margin-top:14px;height:140px;background:linear-gradient(180deg,#3e5b3a,#6f8c4e 60%,#4d6d63)}
.about p{font-size:14px;line-height:22.5px;margin:12px 2px 0}
.more{display:block;margin-top:10px;font-size:13px;font-weight:700;color:var(--wine);padding-left:2px}
.events{left:350px}
.event{display:flex;gap:10px;padding:12px 0;border-bottom:1px dashed var(--rule)}
.event:last-of-type{border-bottom:0;padding-bottom:4px}
.event .thumb{flex:0 0 60px;height:60px;background:linear-gradient(180deg,#7aa0a8,#4f7a3a 55%,#5e7f6f)}
.event h3{font-size:14px;font-weight:700;color:var(--wine);margin-bottom:6px}
.event p{font-size:14px;line-height:20px}
.ad{left:681px;padding:0;overflow:hidden;background:linear-gradient(180deg,#0e4fa3 0%,#0e4fa3 37%,#fff 37%,#f4f6f8 100%)}
.ad-name{font-size:32px;font-weight:700;color:var(--white);text-align:center;margin-top:32px;line-height:1.1}
.ad-photo{position:absolute;left:72px;bottom:4px;width:155px;height:205px;border-radius:18px 18px 10px 10px;background:linear-gradient(180deg,#e9eef1,#d7c48d 55%,#c9a33a)}
.newsletter{position:absolute;left:0;top:1005px;width:1280px;height:70px;background:var(--band);border-top:1px solid #d0d0d0}
.newsletter .inner{position:absolute;left:142px;top:10px;display:flex;align-items:center}
.mail-badge{width:46px;height:46px;border-radius:50%;background:var(--white);border:1px solid #ccc;display:flex;align-items:center;justify-content:center}
.newsletter h2{font-size:24px;font-weight:700;color:#3b3b3b;margin-left:8px}
.newsletter .chev{margin:0 14px 0 8px}
.newsletter p{font-size:16px;color:var(--muted)}
.email-field{position:absolute;left:842px;top:19px;width:190px;height:35px;background:var(--white);border:1px solid #ccc;font-size:13px;font-style:italic;color:#777;padding:9px 8px}
.subscribe{position:absolute;left:1041px;top:19px;width:99px;height:35px;background:var(--wine);color:var(--white);font-weight:700;font-size:15px;display:flex;align-items:center;justify-content:center;border-radius:2px}
.footer{position:absolute;left:0;top:1075px;width:1280px;height:220px;background:var(--foot);color:#eee}
.fcol{position:absolute;top:30px}
.fcol h3{font-family:"Roboto Condensed",sans-serif;font-weight:400;font-size:19px;padding-bottom:8px;border-bottom:1px solid #5a5a5a}
.divider{position:absolute;top:22px;width:1px;height:190px;background:#4c4c4c}
.quick{left:143px;width:150px}
.quick ul{list-style:none;margin-top:3px}
.quick li{font-size:14px;line-height:25.3px;padding-left:12px;position:relative}
.quick li::before{content:"›";position:absolute;left:0;top:-1px;color:#aaa}
.advertise{left:377px;width:190px}
.advertise p{font-size:13px;line-height:19px;margin-top:9px}
.advertise .btn{display:block;margin-top:10px;width:190px;height:54px;background:linear-gradient(180deg,#123d8c,var(--navy-dark));color:var(--white);font-size:16px;font-weight:700;text-align:center;line-height:50px;border-radius:2px}
.talk{left:663px;width:185px}
.talk .line{display:flex;align-items:center;gap:10px;font-size:16px;margin-top:10px}
.talk .line:first-of-type{margin-top:14px}
.socials{display:flex;gap:10px;margin-top:24px}
.socials span{width:35px;height:35px;border-radius:3px}
.foot-brand{position:absolute;left:920px;top:88px;display:flex;align-items:center;gap:14px;font-family:"Roboto Condensed",sans-serif;font-size:40px;color:#8a8a8a}
.foot-brand i{width:46px;height:46px;border-radius:50%;background:#8a8a8a}
.copyright{position:absolute;left:0;top:1295px;width:1280px;height:40px;background:var(--foot-dark);color:#aaa;font-size:13px;text-align:center;line-height:40px}
</style>
</head>
<body>
<div class="page" role="img" aria-label="Soft backdrop of a Texas marsh with water and tall grass">
  <div class="account-tab">
    <span><svg width="12" height="14" viewBox="0 0 12 14"><rect x="1" y="6" width="10" height="8" fill="#fff"/><path d="M3 6V4a3 3 0 0 1 6 0v2" stroke="#fff" stroke-width="2" fill="none"/></svg>LOGIN</span>
    <span><svg width="14" height="14" viewBox="0 0 14 14"><circle cx="7" cy="4" r="3.5" fill="#fff"/><path d="M0 14c0-4 3-6 7-6s7 2 7 6z" fill="#fff"/></svg>BECOME A MEMBER</span>
  </div>
  <div class="brand"><span class="brand-mark"></span><span class="brand-short">TMRCL</span></div>
  <div class="site-title">TEXAS MARSH REED CONSERVATION LEAGUE</div>
  <nav class="main-nav">
    <a class="current" href="#">Home</a><a href="#">About</a><a href="#">Members</a><a href="#">Resources</a><a href="#">Events</a><a href="#">Contact</a>
  </nav>

  <main class="content">
    <section class="slider">
      <div class="slide-photo" role="img" aria-label="Photo of a calm pond covered with lily pads and trees on the far bank"></div>
      <div class="slide-caption">
        <div class="lead">Promoting Environmental Stewardship Through</div>
        <div class="focus">Operations, Research, Education and Outreach</div>
      </div>
      <span class="slide-arrow prev"><svg width="10" height="16"><path d="M8 2 2 8l6 6" stroke="#666" stroke-width="2" fill="none"/></svg></span>
      <span class="slide-arrow next"><svg width="10" height="16"><path d="M2 2l6 6-6 6" stroke="#666" stroke-width="2" fill="none"/></svg></span>
    </section>

    <section class="card about">
      <h2>About <b>TMRCL</b></h2>
      <div class="photo" role="img" aria-label="Photo of lily pads and reeds in dark water"></div>
      <p>Lorem ipsum dolor sit amet adipiscing elit, sed diam nonummy nibh euis tincidunt ut laoreet dolore magna aliquam e volutpa Ut wisi enim ad minim veniam.</p>
      <a class="more" href="#">READ MORE »</a>
    </section>

    <section class="card events">
      <h2>Upcoming <b>Events</b></h2>
      <div class="event"><div class="thumb" role="img" aria-label="Photo of pond plants"></div><div><h3>Lorem ipsum dolor sit amet</h3><p>Sed diam nonummy ni tincidunt ut laoreet dolore magna.</p></div></div>
      <div class="event"><div class="thumb" role="img" aria-label="Photo of trees by a lake"></div><div><h3>Lorem ipsum dolor sit amet</h3><p>Sed diam nonummy ni tincidunt ut laoreet dolore magna.</p></div></div>
      <div class="event"><div class="thumb" role="img" aria-label="Photo of green reeds"></div><div><h3>Lorem ipsum dolor sit amet</h3><p>Sed diam nonummy ni tincidunt ut laoreet dolore magna.</p></div></div>
      <a class="more" href="#">READ MORE »</a>
    </section>

    <aside class="card ad">
      <div class="ad-name">ClearPond Supply</div>
      <div class="ad-photo" role="img" aria-label="Product photo of two spray bottles for plant care"></div>
    </aside>
  </main>

  <section class="newsletter">
    <div class="inner">
      <span class="mail-badge"><svg width="26" height="18" viewBox="0 0 26 18"><rect x="1" y="1" width="24" height="16" fill="var(--wine)"/><path d="M1 1l12 9 12-9" stroke="#fff" stroke-width="2" fill="none"/></svg></span>
      <h2>Newsletter Signup</h2>
      <svg class="chev" width="34" height="34" viewBox="0 0 34 34"><path d="M4 4l13 13L4 30M16 4l13 13-13 13" stroke="#9a9a9a" stroke-width="4" fill="none"/></svg>
      <p>Don't miss out monthly email,offering the very best.</p>
    </div>
    <div class="email-field">Enter your email here</div>
    <div class="subscribe">SUBSCRIBE</div>
  </section>

  <footer class="footer">
    <div class="fcol quick"><h3>Quick Links</h3>
      <ul><li>Home</li><li>About</li><li>Members</li><li>Resources</li><li>Events</li><li>Contact</li></ul>
    </div>
    <span class="divider" style="left:329px"></span>
    <div class="fcol advertise"><h3>Advertise with us</h3>
      <p>Sed diam nonummy ni tincidunt ut laoreet dolore magna.</p>
      <a class="btn" href="#">ADVERTISE WITH US</a>
    </div>
    <span class="divider" style="left:619px"></span>
    <div class="fcol talk"><h3>Talk to Us</h3>
      <div class="line"><svg width="16" height="16" viewBox="0 0 16 16"><path d="M3 1l3 3-2 2c1 3 3 5 6 6l2-2 3 3-2 3C7 16 0 9 0 3z" fill="#ddd"/></svg>+1 512 555 0147</div>
      <div class="line"><svg width="16" height="12" viewBox="0 0 16 12"><rect x="0.5" y="0.5" width="15" height="11" fill="#ddd"/><path d="M1 1l7 6 7-6" stroke="#3c3c3c" fill="none"/></svg>support@tmrcl.org</div>
      <div class="socials">
        <span style="background:#3b5998" aria-label="Social link"></span>
        <span style="background:#2ba6de" aria-label="Social link"></span>
        <span style="background:#e8731c" aria-label="Feed link"></span>
        <span style="background:#e5e5e5" aria-label="Social link"></span>
      </div>
    </div>
    <span class="divider" style="left:885px"></span>
    <div class="foot-brand"><i></i>TMRCL</div>
  </footer>
  <div class="copyright">Copyright @ 2014 TMRCL. All rights reserved.</div>
</div>
</body>
</html>
```